Business Card for Start Up Real Estate Company

We need a business card designed for a new real estate company called Belvanta. We plan on improving the experience of real estate transactions for both consumers and agents by using current and evolving technology. We would like to see designs that use our existing logo (attached). Please use a primarily white or light colored background. The final design should communicate technology, sophistication and customer service. Thank you...

Industry/Entity Type

Real Estate

Requirements
Must have
• Primarily white or light colored background
Nice to have
• Isolated A from our logo used as part of the design
Should not have
• Pictures, especially of houses

```html
<!DOCTYPE html>
<html lang="en">
<head>
<meta charset="utf-8">
<title>Belvanta Business Card</title>
<link href="https://fonts.googleapis.com/css2?family=Arimo:wght@400;700&display=swap" rel="stylesheet">
<style>
  :root {
    --page-bg: #ece9e4;
    --card-bg: #ffffff;
    --brand-blue: #1b5794;
    --brand-red: #e42f45;
    --text-grey: #5f5f5f;
    --card-shadow: rgba(0, 0, 0, 0.18);
  }
  html, body {
    margin: 0;
    width: 1200px;
    height: 798px;
    overflow: hidden;
    background: var(--page-bg);
    font-family: "Arimo", Arial, sans-serif;
  }
  .business-card {
    position: absolute;
    left: 180px;
    top: 159px;
    width: 840px;
    height: 480px;
    background: var(--card-bg);
    border-radius: 20px;
    box-shadow: 0 10px 30px var(--card-shadow);
    overflow: hidden;
  }
  .accent-band {
    position: absolute;
    left: 0;
    top: 214px;
    width: 840px;
    height: 104px;
    background: linear-gradient(90deg, var(--brand-blue) 0%, #6a5d8c 50%, var(--brand-red) 100%);
    opacity: 0.85;
  }
  .brand-name {
    position: absolute;
    left: 48px;
    top: 44px;
    margin: 0;
    font-size: 66px;
    font-weight: 400;
    letter-spacing: 1px;
    color: var(--brand-blue);
    line-height: 1;
  }
  .office-address {
    position: absolute;
    left: 76px;
    top: 132px;
    margin: 0;
    font-style: normal;
    font-size: 23px;
    line-height: 32px;
    color: var(--text-grey);
  }
  .office-address span { display: block; }
  .office-address .city { padding-left: 40px; }
  .person {
    position: absolute;
    right: 44px;
    top: 40px;
    text-align: right;
  }
  .person-name {
    margin: 0;
    font-size: 31px;
    font-weight: 700;
    color: var(--brand-blue);
    line-height: 1.1;
  }
  .person-title {
    margin: 2px 0 0;
    font-size: 22px;
    color: var(--text-grey);
  }
  .contact-list {
    position: absolute;
    right: 34px;
    top: 340px;
    margin: 0;
    padding: 0;
    list-style: none;
    text-align: right;
  }
  .contact-item {
    display: flex;
    justify-content: flex-end;
    align-items: center;
    gap: 8px;
    font-size: 24px;
    color: var(--text-grey);
    height: 46px;
  }
  .contact-icon {
    width: 32px;
    height: 32px;
    fill: none;
    stroke: var(--brand-red);
    stroke-width: 2;
  }
  .website {
    position: absolute;
    left: 54px;
    bottom: 30px;
    display: flex;
    align-items: center;
    gap: 12px;
    font-size: 24px;
    color: var(--text-grey);
  }
</style>
</head>
<body>
  <article class="business-card">
    <div class="accent-band" role="img" aria-label="Decorative flowing ribbon in brand blue and red across the card"></div>

    <h1 class="brand-name">BELVANTA</h1>

    <address class="office-address">
      <span>2480 N Alder Way, 5th Floor</span>
      <span class="city">Linwood, CA 95120</span>
    </address>

    <div class="person">
      <p class="person-name">Marcus Hale</p>
      <p class="person-title">CEO/Agent</p>
    </div>

    <ul class="contact-list">
      <li class="contact-item">
        <span>800-555-0148</span>
        <svg class="contact-icon" viewBox="0 0 32 32" aria-hidden="true">
          <rect x="9" y="2" width="14" height="28" rx="2"/>
          <line x1="9" y1="25" x2="23" y2="25"/>
        </svg>
      </li>
      <li class="contact-item">
        <span>info@belvanta.com</span>
        <svg class="contact-icon" viewBox="0 0 32 32" aria-hidden="true">
          <rect x="2" y="7" width="28" height="19"/>
          <polyline points="2,7 16,18 30,7"/>
          <polyline points="2,26 12,16"/>
          <polyline points="30,26 20,16"/>
        </svg>
      </li>
    </ul>

    <div class="website">
      <svg class="contact-icon" viewBox="0 0 32 32" aria-hidden="true">
        <circle cx="16" cy="16" r="13"/>
        <ellipse cx="16" cy="16" rx="6" ry="13"/>
        <line x1="3" y1="16" x2="29" y2="16"/>
        <line x1="5" y1="9" x2="27" y2="9"/>
        <line x1="5" y1="23" x2="27" y2="23"/>
      </svg>
      <span>belvanta.com</span>
    </div>
  </article>
</body>
</html>
```